Bref créative
Martin L. Hollis
Attorney & Counselor at Law
I need double sided standard sized Business Card [3.5" x 2"]
Use different font, but that coordinates with the logo font. I am open to different variations.
Simple
20847 52nd Ave Ct SW, Ste 214
Lakewood, WA 98512
martin@martinlhollis.com
http://www.martinlhollis.com
The logo that should be used on the card should be the second version that I had the artist prepare.
Add my email address on the front of the card.
Email Address: martin@martinlhollis.com
[Insert business logo at top]
[Smaller font] Established 1982
[Larger font with bullet each line]
Divorce & Family Law
Domestic Violence
DUI & Other Criminal Defense
Bankruptcy
I have been requested to upload the *.ai file. Here it is.
This is the *.ai file for the alternate design. This is a variation on the first design. I would like to see what each one looks like on the business card. This design will save space on the card because the logo is on the same line as the text.

```html
<!DOCTYPE html>
<html lang="en">
<head>
<meta charset="utf-8">
<title>Martin L. Hollis — Business Card</title>
<link rel="stylesheet" href="https://fonts.googleapis.com/css2?family=Cinzel:wght@400;500;600&family=Cormorant+SC:wght@500;600&display=swap">
<style>
  :root {
    --bg: #e9e7e3;
    --card: #ffffff;
    --frame: #6e3c14;
    --brown: #6e3c14;
    --blue: #2c6f98;
    --text: #5a5a5a;
    --rule: #b9a48f;
  }
  * { box-sizing: border-box; margin: 0; padding: 0; }
  html, body { width: 1200px; height: 914px; overflow: hidden; }
  body {
    background: var(--bg);
    display: flex;
    align-items: center;
    justify-content: center;
  }
  .card {
    position: relative;
    width: 1050px;
    height: 600px;
    background: var(--card);
    border: 30px solid var(--frame);
    box-shadow: 0 10px 30px rgba(0,0,0,0.15);
  }
  .brand {
    position: absolute;
    top: 110px;
    left: 0;
    right: 0;
    text-align: center;
  }
  .brand-name {
    font-family: "Cinzel", serif;
    font-weight: 500;
    font-size: 58px;
    letter-spacing: 1px;
    color: var(--brown);
    line-height: 1;
  }
  .brand-tagline {
    margin-top: 10px;
    font-family: "Cormorant SC", serif;
    font-weight: 600;
    font-size: 27px;
    letter-spacing: 1px;
    color: var(--blue);
  }
  .details {
    position: absolute;
    top: 285px;
    left: 0;
    right: 0;
    display: flex;
    justify-content: center;
    gap: 36px;
  }
  .contact-person {
    width: 390px;
    text-align: right;
    font-family: "Cormorant SC", serif;
  }
  .person-name {
    font-weight: 600;
    font-size: 30px;
    color: var(--brown);
    padding-bottom: 8px;
    border-bottom: 1.5px solid var(--rule);
    margin-bottom: 12px;
  }
  .address-line {
    font-size: 21px;
    font-weight: 500;
    color: var(--text);
    line-height: 1.35;
  }
  .contact-list {
    list-style: none;
    padding-top: 4px;
    font-family: "Cormorant SC", serif;
    font-size: 21px;
    font-weight: 500;
    color: var(--text);
  }
  .contact-item {
    display: flex;
    align-items: center;
    gap: 10px;
    line-height: 1.45;
  }
  .contact-icon { width: 18px; height: 18px; flex: none; }
</style>
</head>
<body>
  <main class="card">
    <header class="brand">
      <div class="brand-name">Martin L. Hollis</div>
      <div class="brand-tagline">Attorney &amp; Counselor at Law</div>
    </header>

    <section class="details">
      <div class="contact-person">
        <div class="person-name">Martin L. Hollis</div>
        <div class="address-line">20847 52nd Ave Ct SW, Ste 214</div>
        <div class="address-line">Lakewood, WA 98512</div>
      </div>

      <ul class="contact-list">
        <li class="contact-item">
          <svg class="contact-icon" viewBox="0 0 18 18" aria-hidden="true">
            <circle cx="9" cy="9" r="9" fill="#6e3c14"/>
            <path d="M6 4.5l1.6 1.6-0.9 1.3c0.6 1.4 1.5 2.3 2.9 2.9l1.3-0.9 1.6 1.6-1 1.5c-3.4-0.4-6-3-6.4-6.4z" fill="#fff"/>
          </svg>
          (253) 555-0148
        </li>
        <li class="contact-item">
          <svg class="contact-icon" viewBox="0 0 18 18" aria-hidden="true">
            <circle cx="9" cy="9" r="9" fill="#6e3c14"/>
            <rect x="5" y="7" width="8" height="5" fill="#fff"/>
            <rect x="6.5" y="4.5" width="5" height="2.5" fill="#fff"/>
          </svg>
          (253) 555-0162
        </li>
        <li class="contact-item">
          <svg class="contact-icon" viewBox="0 0 18 18" aria-hidden="true">
            <circle cx="9" cy="9" r="9" fill="#6e3c14"/>
            <rect x="4.5" y="6" width="9" height="6.5" fill="#fff"/>
            <path d="M4.5 6l4.5 3.6L13.5 6" fill="none" stroke="#6e3c14" stroke-width="1"/>
          </svg>
          martin@martinlhollis.com
        </li>
        <li class="contact-item">
          <svg class="contact-icon" viewBox="0 0 18 18" aria-hidden="true">
            <circle cx="9" cy="9" r="9" fill="#6e3c14"/>
            <circle cx="9" cy="9" r="4.5" fill="none" stroke="#fff" stroke-width="1.2"/>
            <path d="M4.5 9h9M9 4.5c-2 2.5-2 6.5 0 9M9 4.5c2 2.5 2 6.5 0 9" fill="none" stroke="#fff" stroke-width="1"/>
          </svg>
          www.martinlhollis.com
        </li>
      </ul>
    </section>
  </main>
</body>
</html>
```